Looking for an amazing business card for a thriving DJ business

We need a business card design for a DJ company based in South Florida. The DJ company specializes in weddings, parties, bar mitzvahs, corporate events, proms, and reunions. We are looking for a modern, simple business card design. The card should state DJ Marlow K.
Updates

The name on the card should be DJ Marlow K

Industry/Entity Type

Entertainment Industry

Contact Information for Business Card

DJ Marlow K
512.447.2086
atxdjmarlowk@quellmail.com
https://www.facebook.com/DjMarlowK/
https://www.instagram.com/djmarlow.k/
www.djmarlowk.net

Font styles to use
Serif
Sans Serif

Requirements
Must have
• My business card has to be awesome.
Should not have
• The card has to have personality.

```html
<!DOCTYPE html>
<html lang="en">
<head>
<meta charset="utf-8">
<title>DJ Marlow K — Business Card</title>
<link rel="stylesheet" href="https://fonts.googleapis.com/css2?family=Red+Hat+Display:wght@800&family=Alegreya+Sans:wght@400&display=swap">
<style>
  :root {
    --page: #fdfdfd;
    --blush: #d8c4bb;
    --charcoal: #424740;
    --ink: #3f433d;
    --white: #ffffff;
    --display: "Red Hat Display", Arial, sans-serif;
    --body: "Alegreya Sans", Helvetica, sans-serif;
  }
  * { margin: 0; padding: 0; box-sizing: border-box; }
  html, body { width: 1200px; height: 1200px; overflow: hidden; background: var(--page); }
  .sheet { position: relative; width: 1200px; height: 1200px; }
  .card { position: absolute; left: 255px; width: 697px; height: 454px; overflow: hidden; }
  .card--front { top: 139px; background: var(--blush); }
  .card--back { top: 615px; background: var(--charcoal); }

  .brand-square {
    position: absolute; left: 16px; top: 97px; width: 250px; height: 250px;
    background: var(--white);
    display: flex; align-items: center; justify-content: center;
  }
  .brand-square__name {
    font-family: var(--display); font-weight: 800; font-size: 30px;
    color: var(--ink); letter-spacing: -0.5px;
  }

  .identity { position: absolute; left: 339px; width: 320px; top: 52px; text-align: center; }
  .identity__name {
    font-family: var(--display); font-weight: 800; font-size: 46px;
    line-height: 1; color: var(--ink); letter-spacing: -1px; white-space: nowrap;
  }
  .identity__url {
    font-family: var(--body); font-size: 19px; color: var(--ink);
    letter-spacing: 2px; margin-top: 6px;
  }

  .contacts { position: absolute; left: 369px; top: 284px; list-style: none; }
  .contacts__item {
    display: flex; align-items: center; height: 39px;
    font-family: var(--body); font-size: 20px; color: var(--ink); letter-spacing: 1.6px;
  }
  .contacts__icon { width: 22px; height: 22px; margin-right: 6px; flex: none; }
  .contacts__dot { width: 14px; height: 14px; border-radius: 50%; background: var(--ink); margin: 0 10px 0 4px; flex: none; }

  .back-mark {
    position: absolute; left: 297px; top: 163px; width: 104px; height: 104px;
    border: 5px solid var(--white); border-radius: 6px;
  }
  .back-identity { position: absolute; left: 0; width: 100%; top: 285px; text-align: center; color: var(--white); }
  .back-identity__name { font-family: var(--display); font-weight: 800; font-size: 34px; line-height: 1; letter-spacing: -0.8px; }
  .back-identity__url { font-family: var(--body); font-size: 14px; letter-spacing: 1.8px; margin-top: 3px; }
</style>
</head>
<body>
<main class="sheet">
  <section class="card card--front">
    <div class="brand-square"><span class="brand-square__name">DJ MARLOW K</span></div>

    <div class="identity">
      <h1 class="identity__name">DJ MARLOW K</h1>
      <p class="identity__url">www.djmarlowk.net</p>
    </div>

    <ul class="contacts">
      <li class="contacts__item">
        <svg class="contacts__icon" viewBox="0 0 24 24" aria-hidden="true"><path fill="#3f433d" d="M6.6 3.5c.6-.5 1.4-.4 1.8.2l2 2.9c.4.6.3 1.3-.2 1.8l-1.3 1.2c.9 2 2.5 3.7 4.5 4.7l1.3-1.2c.5-.5 1.3-.5 1.8-.1l2.8 2.1c.6.4.7 1.3.2 1.8l-1.5 1.7c-.7.8-1.9 1-2.9.6C9.7 17.3 6.5 13.9 5 9.2c-.3-1 0-2.1.7-2.8z"/></svg>
        512.447.2086
      </li>
      <li class="contacts__item">
        <svg class="contacts__icon" viewBox="0 0 24 24" aria-hidden="true"><rect x="1" y="5" width="22" height="14" fill="#3f433d"/><path d="M1 5l11 8 11-8M1 19l8-7M23 19l-8-7" stroke="#d8c4bb" stroke-width="1.5" fill="none"/></svg>
        atxdjmarlowk@quellmail.com
      </li>
      <li class="contacts__item"><span class="contacts__dot"></span>DjMarlowK</li>
      <li class="contacts__item"><span class="contacts__dot"></span>djmarlow.k</li>
    </ul>
  </section>

  <section class="card card--back">
    <div class="back-mark"></div>
    <div class="back-identity">
      <h2 class="back-identity__name">DJ MARLOW K</h2>
      <p class="back-identity__url">www.djmarlowk.net</p>
    </div>
  </section>
</main>
</body>
</html>
```